corinelle - Ballon Design

I need a Ballon designed. Please use the psb file ballon_template.psb as template.

I would like to have a ballon designed similar to the file "example.png".
instead of the pellu tot logo please use my attached logo "corinelle logo.ai"

The text should be the same " IT'S A MOM" but the logo should be different.

I should look like more elegant. should be also white background. But for the design feel free.

thanks.

Please also add the webpage "www.corinelle.eu" on the ballon design.

```html
<!DOCTYPE html>
<html lang="en">
<head>
<meta charset="utf-8">
<title>corinelle – It's a Mom balloon</title>
<link href="https://fonts.googleapis.com/css2?family=Arimo:wght@700&family=Ubuntu:wght@400&display=swap" rel="stylesheet">
<style>
  :root {
    --paper: #ffffff;
    --rose: #cf819f;
    --navy: #4a6aa3;
  }
  html, body {
    margin: 0;
    padding: 0;
    width: 1200px;
    height: 1194px;
    overflow: hidden;
    background: var(--paper);
  }
  .balloon-face {
    position: relative;
    width: 1200px;
    height: 1194px;
  }
  .headline {
    margin: 0;
    font-family: "Arimo", Arial, sans-serif;
    font-weight: 700;
    color: var(--rose);
    text-transform: uppercase;
  }
  .headline-line,
  .brand-name,
  .brand-site {
    position: absolute;
    left: 0;
    width: 1180px;
    margin: 0;
    text-align: center;
    line-height: 1;
    white-space: nowrap;
  }
  .headline-its {
    top: 200px;
    font-size: 188px;
    letter-spacing: 7px;
    text-indent: 7px;
  }
  .headline-a {
    top: 353px;
    font-size: 128px;
  }
  .headline-mom {
    top: 463px;
    font-size: 188px;
    letter-spacing: 5px;
    text-indent: 5px;
  }
  .brand-name {
    top: 695px;
    font-family: "Arimo", Arial, sans-serif;
    font-weight: 700;
    font-size: 100px;
    color: var(--navy);
  }
  .brand-site {
    top: 809px;
    font-family: "Ubuntu", "Helvetica Neue", sans-serif;
    font-weight: 400;
    font-size: 36px;
    color: var(--navy);
    letter-spacing: 0.5px;
  }
</style>
</head>
<body>
  <main class="balloon-face">
    <h1 class="headline">
      <span class="headline-line headline-its">It's</span>
      <span class="headline-line headline-a">A</span>
      <span class="headline-line headline-mom">Mom</span>
    </h1>
    <p class="brand-name">corinelle</p>
    <p class="brand-site">www.corinelle.eu</p>
  </main>
</body>
</html>
```